Finiding oppertunites in Real Estate 6.15.20

size of ad 7” x 9.6”
1-I like the ad to stand out and attract people's attention.
2-you should be able to see the text of the ad clearly .. see the attachment anything in yellow is instructions.
3-the list of topics should not be the main part of the ad
4-if you decide you want a picture or vector of a person .. (you decide)
then it should be a white male about 25-30 years old wearing a solid white or blue shirt and not long hair.
5-leave 1 inch for footer
see attachment
Good luck

Target Market(s)

potential male students 25-35 years of age

Industry/Entity Type

Education

Requirements
Must have
• will stand out and people would want to see it.
should be able to read the words of ad
Nice to have
• how to make money in real estate on one line

```html
<!DOCTYPE html>
<html lang="en">
<head>
<meta charset="utf-8">
<title>Real Estate Career Course Flyer</title>
<link href="https://fonts.googleapis.com/css2?family=Roboto:ital,wght@0,300;0,400;0,500;0,700;1,900&display=swap" rel="stylesheet">
<style>
:root{
  --stage:#a7a7a7;
  --dark:#333435;
  --cyan:#11a9e6;
  --blue:#0f8fd8;
  --navy:#1c2a86;
  --badge:#1656b0;
  --light:#eeeeef;
  --paper:#ffffff;
  --ink:#333333;
  --white:#ffffff;
}
*{margin:0;padding:0;box-sizing:border-box}
html,body{width:696px;height:1200px;overflow:hidden;background:var(--stage);font-family:'Roboto',sans-serif}
.flyer{position:absolute;left:18px;top:147px;width:660px;height:905px;background:var(--paper);overflow:hidden}
.hero{position:absolute;left:0;top:0;width:660px;height:553px;background:var(--dark)}
.hero-photo{position:absolute;left:0;top:143px;width:660px;height:410px;
  background:radial-gradient(ellipse 190px 260px at 520px 250px,#c9d7e6 0%,#8d98a3 45%,rgba(51,52,53,0) 75%),
  linear-gradient(180deg,var(--dark) 0%,var(--dark) 45%,#6b6d70 75%,#4a4c4f 100%)}
.title{position:absolute;left:47px;top:40px;color:var(--white);font-weight:900;font-style:italic;font-size:36px;letter-spacing:.2px}
.band{position:absolute;left:0;top:94px;width:660px;height:49px;background:linear-gradient(90deg,var(--cyan) 0%,#1467bf 60%,var(--navy) 100%)}
.band-text{position:absolute;left:47px;top:6px;color:var(--white);font-weight:500;font-size:31px}
.lead{position:absolute;left:47px;top:168px;color:var(--white);font-size:24px;line-height:27px}
.hook{position:absolute;left:47px;top:240px;color:var(--cyan);font-weight:700;font-size:22px;line-height:27.5px}
.info-pill{position:absolute;left:47px;top:498px;width:565px;height:55px;border-radius:18px 18px 0 0;background:linear-gradient(90deg,var(--blue),var(--cyan))}
.info-pill svg{position:absolute;left:13px;top:9px}
.info-label{position:absolute;left:68px;top:7px;color:var(--white);font-size:14px;font-weight:300}
.info-number{position:absolute;left:68px;top:23px;color:var(--white);font-size:20px;font-weight:700}
.details{position:absolute;left:0;top:553px;width:660px;height:240px;background:linear-gradient(180deg,#f7f7f8,var(--light));border-bottom:1px solid #cfcfcf}
.badge{position:absolute;left:58px;top:16px}
.badge-text{position:absolute;left:58px;top:78px;width:124px;text-align:center;color:var(--white);font-size:14px;line-height:17px}
.course{position:absolute;left:20px;top:160px;width:200px;text-align:center;font-weight:700;font-size:16.5px;line-height:22px}
.course .c1{color:var(--cyan)}
.course .c2{color:var(--blue)}
.course .c3{color:var(--navy);font-size:18px}
.topics-head{position:absolute;left:278px;top:44px;color:var(--cyan);font-size:17px;font-weight:300;letter-spacing:.3px}
.topics{position:absolute;top:96px;list-style:none;color:var(--ink);font-size:13.5px;line-height:18px}
.topics li::before{content:"•";position:absolute;margin-left:-23px}
.topics.left{left:302px}
.topics.right{left:485px}
.footer{position:absolute;left:0;top:794px;width:660px;height:111px;background:var(--paper)}
</style>
</head>
<body>
<main class="flyer">
  <section class="hero">
    <div class="hero-photo" role="img" aria-label="Black and white night city skyline by the water with a smiling young businessman in a light blue shirt holding a laptop"></div>
    <h1 class="title">Real Estate Career Course</h1>
    <div class="band"><h2 class="band-text">How to Make Money In Real Estate?</h2></div>
    <p class="lead">For those who have started or<br>would like to go into Real Estate</p>
    <p class="hook">AN INVESTMENT IN<br>KNOWLEDGE OPENS UP<br>UNTOLD OPPORTUNITIES</p>
    <div class="info-pill">
      <svg width="38" height="38" viewBox="0 0 38 38">
        <circle cx="19" cy="19" r="17" fill="none" stroke="#fff" stroke-width="2"/>
        <path d="M14 10c-2 1-3 3-2 6 2 6 6 10 11 12 2 1 4 0 5-2l-3-3-2 1c-3-1-6-4-7-7l1-2z" fill="none" stroke="#fff" stroke-width="1.8" stroke-linejoin="round"/>
      </svg>
      <span class="info-label">FOR MORE INFO</span>
      <span class="info-number">+1 555 014 2020</span>
    </div>
  </section>

  <section class="details">
    <svg class="badge" width="124" height="124" viewBox="0 0 124 124">
      <defs>
        <radialGradient id="badgeFill" cx="50%" cy="40%" r="60%">
          <stop offset="0" stop-color="#2a78d0"/>
          <stop offset="1" stop-color="#123f92"/>
        </radialGradient>
      </defs>
      <polygon fill="url(#badgeFill)" points="62,0 66,5 71,1 74,6 79,3 82,8 87,6 89,11 95,10 96,15 101,15 102,20 107,21 107,26 112,28 111,33 116,36 114,41 118,45 116,50 120,54 117,58 120,62 117,66 120,70 116,74 118,79 114,83 116,88 111,91 112,96 107,98 107,103 102,104 101,109 96,109 95,114 89,113 87,118 82,116 79,121 74,118 71,123 66,119 62,124 58,119 53,123 50,118 45,121 42,116 37,118 35,113 29,114 28,109 23,109 22,104 17,103 17,98 12,96 13,91 8,88 10,83 6,79 8,74 4,70 7,66 4,62 7,58 4,54 8,50 6,45 10,41 8,36 13,33 12,28 17,26 17,21 22,20 23,15 28,15 29,10 35,11 37,6 42,8 45,3 50,6 53,1 58,5"/>
      <g fill="none" stroke="#fff" stroke-width="2">
        <rect x="44" y="24" width="32" height="24" rx="2"/>
        <path d="M56 48v5M50 54h16"/>
        <circle cx="72" cy="50" r="9" fill="#1a5fb8"/>
        <path d="M67 48h8l-2-2M77 52h-8l2 2" stroke-width="1.6"/>
      </g>
    </svg>
    <p class="badge-text">REMOTE<br>SESSIONS</p>
    <p class="course"><span class="c1">12 session course</span><br><span class="c2">Classes starting</span><br><span class="c3">JUNE 16</span></p>

    <h3 class="topics-head">A PARTIAL LISTING OF TOPICS</h3>
    <ul class="topics left">
      <li>Single-family</li><li>Multifamily</li><li>Management</li><li>Real Estate Concepts</li><li>Real Estate law</li><li>Investment properties</li><li>Foreclosures</li>
    </ul>
    <ul class="topics right">
      <li>Rehab</li><li>Foreclosures</li><li>Short sales</li><li>Development</li><li>Finical modeling</li><li>HUD properties</li><li>Due Diligence</li>
    </ul>
  </section>

  <footer class="footer"></footer>
</main>
</body>
</html>
```